Brochure for real estate company

We need the brochure in the attachement re-designed in a consistent way with our website. The text and the structure of the text should not be altered, but addidtional design-elements and other stuff can be added. We're looking for a simple and catchy design as in our website (www.lerchfeld-wohnbau.ch). We need design propositions in file formats where we can always change the text ourselves if that is neccessary later on.

Industry/Entity Type

Real Estate

Font styles to use
Sans Serif

Colors
ec2027
f04a50

```html
<!DOCTYPE html>
<html lang="de">
<head>
<meta charset="utf-8">
<title>Broschüre – Seiten 2 und 3</title>
<link rel="stylesheet" href="https://fonts.googleapis.com/css2?family=Questrial&family=Jost:wght@700&family=PT+Serif:wght@400;700&family=Arimo&display=swap">
<style>
  :root {
    --canvas: #878787;
    --paper: #ffffff;
    --brand-red: #f04a50;
    --ink-dark: #231f20;
    --ink-grey: #6d6e71;
    --white: #ffffff;
  }
  * { margin: 0; padding: 0; box-sizing: border-box; }
  html, body { width: 1200px; height: 1000px; overflow: hidden; }
  body { background: var(--canvas); position: relative; font-family: "PT Serif", Georgia, serif; }

  .page {
    position: absolute; top: 130px; width: 523px; height: 740px;
    background: var(--paper); overflow: hidden;
  }
  .page--two { left: 40px; }
  .page--three { left: 630px; }

  .page__intro {
    position: absolute; left: 46px; top: 252px; width: 460px;
    font-family: "Questrial", "Century Gothic", sans-serif;
    font-size: 16.5px; line-height: 23px; color: var(--ink-grey);
  }

  .page__panel {
    position: absolute; left: 0; top: 322px; width: 100%; height: 385px;
    background: var(--brand-red);
  }
  .page__footer {
    position: absolute; left: 0; bottom: 0; width: 100%; height: 33px;
    background: var(--ink-dark);
  }
  .panel__edges { position: absolute; left: 0; top: 0; width: 100%; height: 100%; }

  .panel__title {
    position: absolute; left: 0; top: 10px; width: 100%; text-align: center;
    font-family: "Jost", "Futura", sans-serif; font-weight: 700;
    font-size: 21px; color: var(--white); letter-spacing: 0.2px;
  }
  .panel__body {
    position: absolute; left: 46px; top: 60px; width: 440px;
    color: var(--white); font-size: 9.6px; line-height: 12.6px;
  }
  .panel__body p { margin-bottom: 11px; }
  .panel__subhead {
    text-align: center; font-size: 13.5px; line-height: 16px;
    margin: 4px 0 12px; 
  }
  .panel__subhead strong { font-weight: 700; }

  .photo-row { position: absolute; left: 0; top: 0; }
  .kitchen-photo {
    position: absolute; left: 108px; top: 30px; width: 307px; height: 204px;
    background: linear-gradient(160deg, #a0704a 0%, #e7e1d8 35%, #f3f1ee 60%, #8d8a86 100%);
  }

  .page-label {
    position: absolute; top: 890px; width: 523px; text-align: center;
    font-family: "Arimo", Arial, sans-serif; font-size: 27px; color: #111;
  }
  .page-label--two { left: 40px; }
  .page-label--three { left: 630px; }
</style>
</head>
<body>

<section class="page page--two">
  <svg class="photo-row" width="523" height="200" viewBox="0 0 523 200">
    <defs>
      <linearGradient id="house" x1="0" y1="0" x2="0" y2="1">
        <stop offset="0" stop-color="#9fb9d6"/><stop offset="0.5" stop-color="#dde0cf"/><stop offset="1" stop-color="#6d7f4d"/>
      </linearGradient>
      <linearGradient id="livingroom" x1="0" y1="0" x2="0" y2="1">
        <stop offset="0" stop-color="#7a3f1c"/><stop offset="0.5" stop-color="#e2d4bd"/><stop offset="1" stop-color="#b9763a"/>
      </linearGradient>
      <linearGradient id="diningroom" x1="0" y1="0" x2="1" y2="1">
        <stop offset="0" stop-color="#e8dcc4"/><stop offset="0.5" stop-color="#6b3a22"/><stop offset="1" stop-color="#c89a62"/>
      </linearGradient>
      <clipPath id="cut"><rect x="0" y="0" width="523" height="191"/></clipPath>
    </defs>
    <g clip-path="url(#cut)">
      <circle cx="115" cy="127" r="67" fill="url(#house)" role="img" aria-label="Foto: Aussenansicht eines Mehrfamilienhauses"/>
      <circle cx="261" cy="127" r="67" fill="url(#livingroom)" role="img" aria-label="Foto: Wohnraum mit Holzbalkendecke und Kachelofen"/>
      <circle cx="410" cy="127" r="67" fill="url(#diningroom)" role="img" aria-label="Foto: Esszimmer mit Kronleuchter"/>
    </g>
  </svg>

  <p class="page__intro">Die Basis einer seriösen Vermittlung ist die lückenlose Darstellung. Gemeinsam beginnen wir mit dem ersten Schritt.</p>

  <div class="page__panel">
    <svg class="panel__edges" viewBox="0 0 523 385" preserveAspectRatio="none">
      <path d="M0 22 Q18 30 17 190 Q16 345 0 356 Z" fill="var(--ink-dark)"/>
      <path d="M523 22 Q505 30 506 190 Q507 345 523 356 Z" fill="var(--ink-dark)"/>
    </svg>
    <h2 class="panel__title">Dokumentation &amp; Insertion</h2>
    <div class="panel__body">
      <p>✓ Verkaufsdokumentation: Wir erstellen für Sie ein ansprechendes und bankkonformes Dossier.</p>
      <p>✓ Insertion: Wir inserieren für Sie kostenlos und umfassend. Durch intelligenten Einsatz der Verkaufskanäle erscheint Ihr Objekt immer am richtigen Ort.</p>
      <p>✓ Aktualität: Titel, Texte und Bilder halten wir stets aktuell.</p>
      <h3 class="panel__subhead"><strong>Klartext:</strong> Das machen wir besser als die Konkurrenz</h3>
      <p>✓ Wir sparen nicht auf Ihre Kosten: Viele Vermittler inserieren Objekte mit nur einem oder maximal zwei Bildern auf den Immobilienplattformen. Resultat: Weniger Kosten für den Vermittler, weniger Interessenten für den Verkäufer – nicht bei uns!</p>
      <p>✓ Wir verkaufen nur für Sie: Grosse Vermittler wollen Objekte verkaufen, gleich welches. Aus diesem Grund werden Interessenten dort immer (teilweise sogar automatisiert per E-Mail) Vergleichsobjekte präsentiert, was die Chance verringert, ihm Ihr Objekt näherzubringen – bei uns sind Sie und Ihre Liegenschaft im Mittelpunkt.</p>
      <p>✓ Wir nehmen uns Zeit: Grosse Vermittler arbeiten oft mit computergenerierten Standarddokumentationen, die sich auf maximal 2 Seiten beschränken. Wir rücken Ihre Liegenschaft durch eine individualisierte Dokumentation ins richtige Licht.</p>
    </div>
  </div>
  <div class="page__footer"></div>
</section>

<section class="page page--three">
  <div class="kitchen-photo" role="img" aria-label="Foto: Küche unter Dachschräge mit Holzbalken"></div>

  <p class="page__intro">Der richtige Umgang mit Menschen ist das Herzstück jeder Vermittlung. Hier richten wir ein besonderes Augenmerk.</p>

  <div class="page__panel">
    <svg class="panel__edges" viewBox="0 0 523 385" preserveAspectRatio="none">
      <path d="M0 22 Q18 30 17 190 Q16 345 0 356 Z" fill="var(--ink-dark)"/>
      <path d="M523 22 Q505 30 506 190 Q507 345 523 356 Z" fill="var(--ink-dark)"/>
    </svg>
    <h2 class="panel__title">Besichtigungen &amp; Unterstützung</h2>
    <div class="panel__body">
      <p>✓ Geschwindigkeit: Bei uns gibt es keine Bürozeiten. Interessentenanfragen beantworten wir spätestens sofort – auch am Wochenende.</p>
      <p>✓ Individuelle Beratung: Wir führen stets zeitnah zur Anfrage verkaufsaktive Einzelbesichtigungen durch und nehmen uns Zeit für den einzelnen Käufer.</p>
      <p>✓ Wir stehen zur Seite: Wir bieten dem potentiellem Käufer eine kostenlose und umfassende Finanzierungsberatung und beschleunigen so die Bankabklärungen.</p>
      <p>✓ Wir geben Antworten: Neben einer kompetenten Besichtigung bieten wir eine unkomplizierte Erstberatung zu Renovations- und Machbarkeitsfragen.</p>
      <h3 class="panel__subhead"><strong>Klartext:</strong> Das machen wir besser als die Konkurrenz</h3>
      <p>✓ Wir sind schnell: Viele Makler sind überlastet, so dass Interessentenanfragen verzögert beantwortet werden oder teilweise sogar ganz vergessen gehen. Bei uns betreut jeder Makler eine limitierte Anzahl Verkaufsobjekte.</p>
      <p>✓ Wir organisieren sinnvoll: Massenbesichtigungen sind bei vielen Maklern an der Tagesordnung. Wir beraten individuell und ohne Druck.</p>
      <p>✓ Immobilienkäufe scheitern oft an der Finanzierung. Wir unterstützen die Käufer aktiv beim Finanzierungsprozess und binden wenn nötig mehrere Banken ein um das Geschäft abzuschliessen.</p>
    </div>
  </div>
  <div class="page__footer"></div>
</section>

<div class="page-label page-label--two">Page 2</div>
<div class="page-label page-label--three">Page 3</div>

</body>
</html>
```